Redesign of an insurance website

Attached is an insurance website that I need to redesign. Currently the website is too dark. I like for example www.brenvalo.com . Could you make the website lighter and change the structure a little so that it is more user friendly?

Industry/Entity Type

Insurance

Number of Pages Required

4 page

```html
<!DOCTYPE html>
<html lang="en">
<head>
<meta charset="utf-8">
<title>KRYTOVKA.CZ – Insurance</title>
<link href="https://fonts.googleapis.com/css2?family=Roboto:wght@400;500;700&family=Lato:wght@400;700&display=swap" rel="stylesheet">
<style>
:root{
  --dark:#3b3b3b;
  --blue:#3d8ff5;
  --brand-blue:#1f7bef;
  --orange:#ff6a13;
  --panel:#efefef;
  --field:#e4e4e4;
  --text:#2b2b2b;
  --muted:#666;
  --white:#fff;
}
*{box-sizing:border-box;margin:0;padding:0}
html,body{width:1192px;height:1200px;overflow:hidden;background:var(--white);font-family:'Roboto',sans-serif;color:var(--text)}
.page{position:relative;width:1192px;height:1200px}
.abs{position:absolute}
.topbar{left:0;top:0;width:1192px;height:57px;background:var(--dark)}
.topnav{left:78px;top:20px;display:flex;gap:33px;color:var(--white);font-weight:500;font-size:14px;letter-spacing:1px}
.btn{display:flex;align-items:center;justify-content:center;color:var(--white);font-weight:500;letter-spacing:1px;font-size:13px;border-radius:2px}
.btn-blue{background:var(--blue)}
.btn-orange{background:var(--orange)}
.signin{left:949px;top:16px;width:94px;height:25px}
.signup{left:1049px;top:16px;width:94px;height:25px}
.logo{left:77px;top:90px;font-size:31px;font-weight:700;color:var(--brand-blue);letter-spacing:.5px}
.mainnav{left:816px;top:96px;display:flex;gap:37px;font-size:12.5px;font-weight:500;letter-spacing:1px}
.social{top:94px;width:20px;height:20px;border:1px solid #ddd;border-radius:50%}
.hero-photo{left:0;top:182px;width:737px;height:498px;background:linear-gradient(135deg,#e9e9e9 0%,#f6f6f6 40%,#d9c2b6 55%,#ececec 75%,#f5f5f5 100%)}
.hero-panel{left:737px;top:182px;width:455px;height:498px;background:var(--panel)}
.badge{left:911px;top:125px;width:88px;height:88px;border-radius:50%;background:var(--white)}
.badge-inner{left:918px;top:132px;width:74px;height:74px;border-radius:50%;background:var(--orange);display:flex;align-items:center;justify-content:center}
.panel-title{left:737px;top:226px;width:453px;text-align:center;font-size:17px;font-weight:500;letter-spacing:1.3px}
.field{left:772px;width:376px;height:42px;background:var(--field);display:flex;align-items:center;font-size:13px;color:#555;letter-spacing:.5px;font-weight:500}
.field svg{margin:0 10px 0 14px}
.agree{left:776px;top:431px;display:flex;align-items:center;gap:12px;font-size:12.5px;color:#666;letter-spacing:.8px;font-weight:500}
.panel-submit{left:913px;top:477px;width:100px;height:27px}
.products-title{left:737px;top:533px;width:453px;text-align:center;font-size:15.5px;font-weight:500;letter-spacing:.4px}
.product{top:570px;width:66px;text-align:center}
.product .disc{width:66px;height:66px;border-radius:50%;background:#e6e6e6;display:flex;align-items:center;justify-content:center}
.product.active .disc{background:var(--orange)}
.product span{display:block;margin-top:10px;font-size:16px;font-weight:500;margin-left:-20px;width:106px}
.arrow{top:594px}
.why-title{left:0;top:735px;width:1192px;text-align:center;font-size:19px;font-weight:500;letter-spacing:1.5px}
.rule{left:533px;top:764px;width:126px;height:4px;background:var(--dark)}
.why-text{left:222px;top:784px;width:752px;text-align:center;font-family:'Lato',sans-serif;font-size:14.4px;line-height:22.4px;color:var(--muted)}
.readmore{left:537px;top:896px;width:109px;height:30px;font-size:13px}
.news-title{left:0;top:974px;width:1192px;text-align:center;font-size:21px;font-weight:700;letter-spacing:1.8px}
.news-sub{left:0;top:1001px;width:1192px;text-align:center;font-size:15px;letter-spacing:1.5px;color:#555}
.news-input{left:304px;top:1039px;width:431px;height:33px;background:var(--field);border-radius:2px 0 0 2px;font-size:12px;color:#555;letter-spacing:1px;display:flex;align-items:center;padding-left:19px}
.news-submit{left:738px;top:1039px;width:110px;height:33px;font-size:15px}
.footer{left:0;top:1138px;width:1192px;height:62px;background:var(--dark);color:var(--white);font-family:'Lato',sans-serif;font-weight:700;font-size:16.5px}
.copy{left:79px;top:20px}
.policy{right:47px;top:20px;letter-spacing:.5px}
</style>
</head>
<body>
<div class="page">
  <div class="abs topbar"></div>
  <nav class="abs topnav"><span>INSURANCE</span><span>INFORMATION</span></nav>
  <div class="abs btn btn-blue signin">SIGN IN</div>
  <div class="abs btn btn-orange signup">SIGN UP</div>

  <div class="abs logo">KRYTOVKA.CZ</div>
  <nav class="abs mainnav"><span>ABOUT US</span><span>FAQ</span><span>CONTACT</span></nav>
  <div class="abs social" style="left:1070px"></div>
  <div class="abs social" style="left:1096px"></div>
  <div class="abs social" style="left:1122px"></div>

  <div class="abs hero-photo" role="img" aria-label="Hands forming a protective roof over a white model car on a white table"></div>
  <div class="abs hero-panel"></div>
  <div class="abs badge"></div>
  <div class="abs badge-inner">
    <svg width="44" height="30" viewBox="0 0 44 30"><path d="M8 12 L12 3 H32 L36 12 H40 V24 H36 V28 H30 V24 H14 V28 H8 V24 H4 V12Z" fill="#fff"/><path d="M13 11 L15 6 H29 L31 11Z" fill="#ff6a13"/><rect x="7" y="16" width="6" height="3" fill="#ff6a13"/><rect x="31" y="16" width="6" height="3" fill="#ff6a13"/></svg>
  </div>

  <h2 class="abs panel-title">REGISTER INSURANCE</h2>
  <div class="abs field" style="top:260px">
    <svg width="14" height="14" viewBox="0 0 14 14" fill="none" stroke="#555" stroke-width="1.3"><circle cx="7" cy="4.5" r="3"/><path d="M1.5 13c0-3 2.5-5 5.5-5s5.5 2 5.5 5"/></svg>Name</div>
  <div class="abs field" style="top:316px">
    <svg width="14" height="14" viewBox="0 0 14 14" fill="none" stroke="#555" stroke-width="1.3"><path d="M3 1l2.5 3-1.5 2c1 2 2 3 4 4l2-1.5 3 2.5-1.5 2C6 13 1 8 1 2.5z"/></svg>Phone</div>
  <div class="abs field" style="top:370px">
    <svg width="15" height="12" viewBox="0 0 15 12" fill="none" stroke="#555" stroke-width="1.2"><rect x=".6" y=".6" width="13.8" height="10.8"/><path d="M.6.6l6.9 6 6.9-6M.6 11.4l5-5M14.4 11.4l-5-5"/></svg>Email</div>
  <div class="abs agree">
    <svg width="16" height="16" viewBox="0 0 16 16" fill="none" stroke="#555" stroke-width="1.5"><path d="M13 8v6H1V2h9"/><path d="M4 7l3 3 8-9"/></svg>Agree with Term And Conditions</div>
  <div class="abs btn btn-blue panel-submit" style="font-size:13.5px">SUBMIT</div>

  <h3 class="abs products-title">SELECT A DIFFERENT INSURANCE PRODUCT</h3>
  <svg class="abs arrow" style="left:766px" width="10" height="16" viewBox="0 0 10 16" fill="none" stroke="#333" stroke-width="1.6"><path d="M8 2L2 8l6 6"/></svg>
  <svg class="abs arrow" style="left:1140px" width="10" height="16" viewBox="0 0 10 16" fill="none" stroke="#333" stroke-width="1.6"><path d="M2 2l6 6-6 6"/></svg>

  <div class="abs product active" style="left:788px"><div class="disc">
    <svg width="40" height="28" viewBox="0 0 44 30"><path d="M8 12 L12 3 H32 L36 12 H40 V24 H36 V28 H30 V24 H14 V28 H8 V24 H4 V12Z" fill="#fff"/><path d="M13 11 L15 6 H29 L31 11Z" fill="#ff6a13"/><rect x="7" y="16" width="6" height="3" fill="#ff6a13"/><rect x="31" y="16" width="6" height="3" fill="#ff6a13"/></svg></div><span>Car</span></div>
  <div class="abs product" style="left:876px"><div class="disc">
    <svg width="34" height="34" viewBox="0 0 34 34" fill="#ff6a13"><path d="M29 3c2 0 2 2 0 4l-6 6 3 14-3 3-5-11-5 5 1 5-2 2-3-6-6-3 2-2 5 1 5-5-11-5 3-3 14 3 6-6c1-1 2-2 2-2z"/></svg></div><span>Travel</span></div>
  <div class="abs product" style="left:969px"><div class="disc">
    <svg width="22" height="40" viewBox="0 0 22 40" fill="#ff6a13"><circle cx="11" cy="4.5" r="4"/><path d="M4 10h14c1.5 0 2.5 1 2.5 2.5V24h-3V14h-1v25h-4V26h-3v13h-4V14h-1v10h-3V12.5C1.5 11 2.5 10 4 10z"/></svg></div><span>LIfe</span></div>
  <div class="abs product" style="left:1059px"><div class="disc">
    <svg width="38" height="32" viewBox="0 0 38 32" fill="#ff6a13"><path d="M19 1L1 16l2 2.5L19 5l16 13.5L37 16 30 10V3h-4v3.5z"/><path d="M7 17L19 7l12 10v14h-9v-9h-6v9H7z"/></svg></div><span>Home</span></div>

  <h2 class="abs why-title">WHY TO GET AN INSURANCE FROM US ?</h2>
  <div class="abs rule"></div>
  <p class="abs why-text">Lorem Ipsum has been the industry's standard dummy text ever since the 1500s, when an unknown printer took a galley of type and scrambled it to make a type specimen book. It has survived not only five centuries but also the leap into electronic typesetting, remaining essentially unchanged. It was popularised&nbsp; the 1960 with the release of Letraset sheets containing.</p>
  <div class="abs btn btn-blue readmore">Read More</div>

  <h2 class="abs news-title">SUBSCRIBE TO OUR NEWSLETTER</h2>
  <p class="abs news-sub">To receive the latest news &amp; update</p>
  <div class="abs news-input">Your E-Mail</div>
  <div class="abs btn btn-blue news-submit">SUBMIT</div>

  <footer class="abs footer">
    <span class="abs copy">Copyright © 2017 KRYTOVKA.CZ All Rights Reserved.</span>
    <span class="abs policy">PRIVACY &amp; POLICY</span>
  </footer>
</div>
</body>
</html>
```